pharmacy/travel clinic business card design

We need a business card for our new business called Tessaly Travel Clinic and Pharmacy. Our primary focus is doing consultations for people before travelling internationally and providing vaccinations and prescriptions for them. While the business is considered a pharmacy, it has more the look and feel of a doctor's office. The design should communicate a professional and trustworthy feel. I have attached a copy of the logo we are going to be using.
Thanks for the submissions.  If you haven`t been eliminated you are one of the finalists.  Decision will likely be made tomorrow.

Customers, other health care professionals, travel agents
Clinic

```html
<!DOCTYPE html>
<html lang="en">
<head>
<meta charset="utf-8">
<title>Tessaly Travel Clinic and Pharmacy – Business Card</title>
<link rel="stylesheet" href="https://fonts.googleapis.com/css2?family=Arimo:wght@400;700&display=swap">
<style>
  :root {
    --backdrop: #3a3a3a;
    --card-white: #ffffff;
    --brand-blue: #2b5fae;
    --brand-green: #7cc242;
    --sky-blue: #2aa6e0;
    --deep-blue: #2b4a9e;
    --text-white: #ffffff;
  }
  html, body {
    margin: 0;
    width: 1200px;
    height: 900px;
    overflow: hidden;
    background: var(--backdrop);
    font-family: "Arimo", Arial, sans-serif;
  }
  .stage { position: relative; width: 1200px; height: 900px; }
  .card {
    position: absolute;
    top: 300px;
    width: 525px;
    height: 300px;
    overflow: hidden;
    box-sizing: border-box;
  }
  .card--front { left: 58px; background: var(--card-white); }
  .card--back {
    left: 592px;
    background: linear-gradient(100deg, var(--sky-blue) 0%, #2a7fc8 45%, var(--deep-blue) 100%);
  }

  .wordmark {
    position: absolute;
    display: flex;
    align-items: center;
    gap: 10px;
    font-weight: 700;
    line-height: 1.05;
  }
  .wordmark__dot { flex: none; border-radius: 50%; }
  .wordmark__name span { display: block; }

  .card--front .wordmark { left: 40px; top: 44px; color: var(--brand-blue); font-size: 25px; }
  .card--front .wordmark__dot { width: 16px; height: 16px; background: var(--brand-blue); }

  .card--back .wordmark { left: 132px; top: 92px; color: var(--text-white); font-size: 32px; }
  .card--back .wordmark__dot { width: 20px; height: 20px; background: var(--text-white); }

  .holder { position: absolute; left: 50px; top: 160px; }
  .holder__name { margin: 0; color: var(--brand-blue); font-size: 17px; font-weight: 700; }
  .holder__role { margin: 2px 0 0; color: var(--brand-green); font-size: 13px; }

  .contact {
    position: absolute;
    left: 50px;
    top: 201px;
    margin: 0;
    padding: 0;
    list-style: none;
    color: var(--brand-blue);
    font-size: 13px;
    line-height: 19px;
  }
  .contact .label { color: var(--brand-green); }
  .contact .sep { margin: 0 6px; }

  .web {
    position: absolute;
    left: 0;
    right: 0;
    top: 238px;
    margin: 0;
    padding-left: 100px;
    text-align: center;
    color: var(--text-white);
    font-size: 13px;
  }
</style>
</head>
<body>
<main class="stage">

  <section class="card card--front" aria-label="Card front">
    <div class="wordmark">
      <span class="wordmark__dot"></span>
      <div class="wordmark__name">
        <span>Tessaly Travel Clinic</span>
        <span>and Pharmacy</span>
      </div>
    </div>

    <div class="holder">
      <p class="holder__name">Marcus Hale</p>
      <p class="holder__role">Position</p>
    </div>

    <ul class="contact">
      <li><span class="label">p :</span> 00 61 555 010 234<span class="sep">|</span><span class="label">f :</span> 00 61 555 010 235</li>
      <li><span class="label">e :</span> info@tessalyclinic.com<span class="sep">|</span><span class="label">w :</span> www.tessalyclinic.com</li>
      <li>chirpnet.com#<span class="label">tessalyclinic</span><span class="sep">|</span>friendbook.com/<span class="label">tessalyclinic</span></li>
    </ul>
  </section>

  <section class="card card--back" aria-label="Card back">
    <div class="wordmark">
      <span class="wordmark__dot"></span>
      <div class="wordmark__name">
        <span>Tessaly Travel Clinic</span>
        <span>and Pharmacy</span>
      </div>
    </div>
    <p class="web">www.TessalyTravelClinic.com.au</p>
  </section>

</main>
</body>
</html>
```